Logo+Business Card Design for Architecture Photographer

Hi Everyone,

I am looking for logo/business designs for my new business - Dovel Pictura. My business does commercial photography with a specialization in architecture, luxury real estate, and design. The Int is short for interior and ex is short for exterior.

Some of the values of my business are:
- providing top quality photography and post-processing (straight lines, accurate and bold whites/blacks/colors) for commercial use (websites, social media, advertising campaigns)
- fostering a collaborative workflow that is professional and fun that will have clients returning because of the premium service they received
- asking the right questions so that I can capture what matters to my clients with my own creative vision

I want my final look to be modern and bold. The business cards will be letter pressed/debossed, so the design should incorporate that. I am imagining a solid matte olive green or matte navy blue background on one side and white on the other. The card will be printed on colored cards, so you don't have to put a colored background as part of the design. I have attached some examples of colors I like, although it doesn't matter too much for the purpose of your work.

I want the debossing to be part of the design of the business card. This debossing should be some some of pattern or a frame that holds the logo on the back of the card (I have attached some sample images named geometric debossing to show what I mean). Then I can just foil print my logo on the back. My contact info and a logo will be on the front.

Somewhere it should say "Architecture, Luxury Real Estate, Design".

My vision for the logo: no cameras or buildings. I can't think of anything symbolic for the logo, but it should somehow contain Dovel. It might be cool to have them separated by a line like Do | Vel. Or have the Int inside something, and the Ex outside.

I plan on using Quarvel to print the cards. You can find their specifications here: https://quarvel.example/products/duplex-business-cards?variant=5837204916273

It would be nice to have a psd file that I can edit as well as a PDF to deliver to the printing company. Both must be vector graphics.

Thank you to everyone who has submitted a design as it has helped me get a better idea of what I want.

Target Market(s)

Designers, architects

Industry/Entity Type

Photographer

Contact Information for Business Card

See project description

Logo Text

Dovel Pictura

Font styles to use
Sans Serif
Decorative

Colors
ffffff

Requirements
Must have
• Logo and business card design. Deboss area less than 3 square inches. Deboss area should be some sort of a pattern/design as shown in attachments labelled "Geometric Debossing Example".
• Logo design and deboss design must be submitted in vector graphics.
Nice to have
• Color doesn't have to be shown on the design because I will be printing on colored paper, although it would be helpful to help me visualize what it will eventually look like.
Should not have
• A camera or building in the design...too cliche.

```html
<!DOCTYPE html>
<html lang="en">
<head>
<meta charset="utf-8">
<title>Dovel Pictura — Business Card</title>
<link rel="stylesheet" href="https://fonts.googleapis.com/css2?family=Archivo:wght@400;500;600&display=swap">
<style>
  :root {
    --backdrop: #3b3430;
    --card: #3d31b8;
    --card-edge: #2a2190;
    --deboss: #17106a;
    --deboss-highlight: #5347d0;
    --deboss-line: #1f1780;
  }
  * { margin: 0; padding: 0; box-sizing: border-box; }
  html, body { width: 1200px; height: 716px; overflow: hidden; }
  body {
    background: var(--backdrop);
    font-family: "Archivo", sans-serif;
    position: relative;
  }
  .card {
    position: absolute;
    top: 210px;
    width: 520px;
    height: 297px;
    background: var(--card);
    border-radius: 3px;
    box-shadow: 0 3px 0 var(--card-edge), 0 14px 30px rgba(0,0,0,0.45);
    color: var(--deboss);
  }
  .card--back { left: 50px; }
  .card--front { left: 630px; }

  .deboss-frame {
    position: absolute;
    inset: 0;
    width: 520px;
    height: 297px;
  }
  .deboss-frame .groove {
    fill: none;
    stroke: var(--deboss-line);
    stroke-width: 1.5;
  }
  .deboss-frame .groove-light {
    fill: none;
    stroke: var(--deboss-highlight);
    stroke-width: 1;
  }

  .wordmark {
    font-weight: 600;
    letter-spacing: 0.02em;
    color: var(--deboss);
    text-shadow: 0 1px 0 var(--deboss-highlight);
    white-space: nowrap;
  }
  .card--back .wordmark {
    position: absolute;
    left: 50%; top: 118px;
    transform: translate(-50%, -50%);
    font-size: 64px;
    line-height: 1;
  }
  .tagline {
    position: absolute;
    left: 0; right: 0; top: 184px;
    text-align: center;
    font-size: 11px;
    font-weight: 600;
    letter-spacing: 0.16em;
    text-transform: uppercase;
    color: var(--deboss);
    text-shadow: 0 1px 0 var(--deboss-highlight);
  }

  .card--front .wordmark {
    position: absolute;
    left: 34px; top: 50%;
    transform: translateY(-50%);
    font-size: 50px;
    line-height: 1;
  }
  .divider {
    position: absolute;
    left: 262px; top: 44px;
    width: 1.5px; height: 209px;
    background: var(--deboss);
    box-shadow: 1px 0 0 var(--deboss-highlight);
  }
  .contact {
    position: absolute;
    left: 282px; top: 56px;
    font-size: 13px;
    font-weight: 500;
    line-height: 1.5;
    color: var(--deboss);
    text-shadow: 0 1px 0 var(--deboss-highlight);
  }
  .contact__name {
    font-weight: 600;
    font-size: 18px;
    letter-spacing: 0.04em;
    text-transform: uppercase;
    line-height: 1.1;
  }
  .contact__role { margin-bottom: 12px; }
  .contact__address { margin-bottom: 8px; }
  .contact__line { display: flex; align-items: center; gap: 7px; }
  .contact__line svg { width: 10px; height: 10px; flex: none; }
</style>
</head>
<body>
  <section class="card card--back" aria-label="Card back">
    <svg class="deboss-frame" viewBox="0 0 520 297" aria-hidden="true">
      <rect class="groove" x="40" y="36" width="440" height="225"/>
      <rect class="groove-light" x="41" y="37.5" width="440" height="225"/>
      <rect class="groove" x="52" y="48" width="416" height="201"/>
      <g class="groove">
        <path d="M40 66 L70 36 M40 96 L100 36 M40 126 L130 36"/>
        <path d="M480 66 L450 36 M480 96 L420 36 M480 126 L390 36"/>
        <path d="M40 231 L70 261 M40 201 L100 261 M40 171 L130 261"/>
        <path d="M480 231 L450 261 M480 201 L420 261 M480 171 L390 261"/>
      </g>
      <rect x="53" y="49" width="414" height="199" fill="var(--card)"/>
      <rect class="groove" x="52" y="48" width="416" height="201"/>
      <path class="groove" d="M150 170 H370"/>
    </svg>
    <div class="wordmark">Do | Vel</div>
    <div class="tagline">Architecture, Luxury Real Estate, Design</div>
  </section>

  <section class="card card--front" aria-label="Card front">
    <div class="wordmark">Do | Vel</div>
    <div class="divider"></div>
    <div class="contact">
      <div class="contact__name">Corwin Hale</div>
      <div class="contact__role">Founder</div>
      <div class="contact__address">418 Lintel Avenue #207<br>Marrow City, TX 75990</div>
      <div class="contact__line">
        <svg viewBox="0 0 10 10" aria-hidden="true"><path d="M2 1 L4 1 L4.6 3.2 L3.4 4 Q4.2 5.8 6 6.6 L6.8 5.4 L9 6 L9 8 Q5 9 2.4 6.8 Q0.8 4.6 2 1 Z" fill="currentColor"/></svg>
        <span>214-555-0173</span>
      </div>
      <div class="contact__line">
        <svg viewBox="0 0 10 10" aria-hidden="true"><rect x="0.8" y="2" width="8.4" height="6" fill="none" stroke="currentColor" stroke-width="1"/><path d="M1 2.4 L5 5.4 L9 2.4" fill="none" stroke="currentColor" stroke-width="1"/></svg>
        <span>info@DovelPictura.example</span>
      </div>
      <div class="contact__line">
        <svg viewBox="0 0 10 10" aria-hidden="true"><circle cx="5" cy="5" r="4" fill="none" stroke="currentColor" stroke-width="1"/><path d="M1 5 H9 M5 1 Q2.6 5 5 9 Q7.4 5 5 1" fill="none" stroke="currentColor" stroke-width="0.8"/></svg>
        <span>www.DovelPictura.example</span>
      </div>
    </div>
  </section>
</body>
</html>
```